Brill's Jewelers website (www.brillsjewelers-example.com)

We are in need of a web storefront for a retail Jewelry store.
www.brillsjewelers-example.com
https://www.facebook.com/Brills-Jewelers-Palm-Vista-740315928461257/

Brill's Jewelers is located in Coral Gables, Florida. The store has been family owned and operated since 1958. Their focus customers are high-income families that care about quality over the brand name. They mostly sell fashion jewelry and diamonds up to 8 carats. We are looking for a simple minimalistic site that their customers can view their inventory and purchase items online.

Competitors websites:
https://www.orvinjewelers-example.com/
http://www.pelvaro-example.com/
http://truecutjewelers-example.com/

Pages:
-Home (with message bulletin)
-Jewelry
We would be able to create the subpages ie Rings, Bracelets, Earrings, Necklaces, Estate, Watches, Men's, Children's
-Services
We would need sub pages ie Appraisals, Consignment, Repairs
-About us
-Contact

Target Market(s)

Local wealthy families

Coding

Number of Pages Required

Font styles to use
Serif

Requirements
Must have
• -An E-commerce site customers can buy jewelry online.
-An easy process internally to add new items to the site
-Colors are Black and White or Black and Gold
Nice to have
• I would like to stay away from face shots of random models in stock photos. I want the jewelry pieces as the focus, not models.

```html
<!DOCTYPE html>
<html lang="en">
<head>
<meta charset="utf-8">
<title>Brill's Jewelers — Your Hometown Jeweler</title>
<link href="https://fonts.googleapis.com/css2?family=Libre+Baskerville:wght@400;700&family=Poppins:wght@300;400;500&display=swap" rel="stylesheet">
<style>
:root{
  --gold:#c9a54a;
  --gold-soft:#d9bd6d;
  --gold-deep:#b8923a;
  --ink:#1b1b1b;
  --text:#555;
  --cream:#f1efe9;
  --beige:#f4eedc;
  --night:#1f2227;
  --white:#fff;
}
*{margin:0;padding:0;box-sizing:border-box}
html,body{width:1200px;height:4661px;overflow:hidden}
body{position:relative;background:var(--white);font-family:"Poppins",sans-serif;color:var(--text);font-size:14px}
.abs{position:absolute}
.serif{font-family:"Libre Baskerville",serif}
.photo{position:absolute}
h1,h2,h3{font-family:"Libre Baskerville",serif;color:var(--ink);font-weight:400}
.section-title{position:absolute;left:0;width:1200px;text-align:center;font-size:38px;letter-spacing:.5px}
.wave{position:absolute;width:60px;height:10px}
.btn{position:absolute;display:flex;align-items:center;justify-content:center;background:var(--gold-soft);color:var(--white);font-family:"Libre Baskerville",serif;font-size:18px;letter-spacing:.5px;border-radius:3px;text-decoration:none}

/* hero */
.hero{position:absolute;left:0;top:0;width:1200px;height:677px;background:linear-gradient(100deg,#5b4517 0%,#806024 40%,#9c7a38 65%,#6d5220 100%)}
.nav{position:absolute;top:40px;left:0;width:1200px;height:24px;font-size:15px;color:var(--white)}
.nav a{position:absolute;color:var(--white);text-decoration:none}
.nav .active{color:var(--gold-soft)}
.nav .active::before{content:"";position:absolute;left:-14px;top:8px;width:7px;height:7px;border-radius:50%;background:var(--gold-soft)}
.brand{position:absolute;text-align:center;color:var(--white)}
.brand .name{font-family:"Libre Baskerville",serif;font-weight:700;font-size:36px;letter-spacing:1px;line-height:1}
.brand .tag{font-size:11px;letter-spacing:1px;border-top:1px solid rgba(255,255,255,.8);margin-top:5px;padding-top:3px}
.hero-dots span{position:absolute;left:32px;width:8px;height:8px;border-radius:50%;background:var(--gold-soft)}
.hero h1{position:absolute;left:103px;top:238px;color:var(--white);font-size:41px;line-height:52px;letter-spacing:.5px}
.hero .visit{position:absolute;left:105px;top:412px;color:var(--gold-soft);font-size:21px}

/* intro */
.intro h2{position:absolute;left:78px;top:768px;font-size:38px;line-height:47px}
.intro .lead{position:absolute;left:76px;top:945px;font-size:16px;color:#333}
.intro p.body{position:absolute;left:78px;width:460px;font-size:14px;line-height:27px;color:#666}

/* grid */
.subtitle{position:absolute;left:0;width:1200px;text-align:center;font-size:15px;color:#444}
.explore{position:absolute;left:0;width:1200px;top:1903px;text-align:center;color:var(--gold);font-size:18px}

/* lifetime */
.lifetime{position:absolute;left:0;top:1996px;width:1200px;height:451px;background:var(--cream)}
.perk{position:absolute;left:0;width:1200px;text-align:center;font-size:17px;color:#333}

/* about */
.about-card{position:absolute;left:121px;top:2571px;width:521px;height:312px;background:var(--white);box-shadow:0 4px 24px rgba(0,0,0,.12);text-align:center}
.about-card h2{margin-top:48px;font-size:38px}
.about-card p{position:absolute;left:60px;width:400px;top:126px;font-size:14px;line-height:27px;color:#666}

/* services */
.service{position:absolute;top:3569px;width:198px;height:214px;background:var(--white);box-shadow:0 2px 14px rgba(0,0,0,.09);text-align:center}
.service svg{margin-top:28px}
.service h3{font-size:20px;margin-top:14px}
.service p{font-size:14px;line-height:25px;color:#666;margin-top:10px;padding:0 18px}

/* clients */
.clients{position:absolute;left:0;top:3855px;width:1200px;height:384px;background:var(--cream)}
.review{position:absolute;top:4030px;width:340px;font-size:14px;line-height:27px;color:#666}
.client-name{position:absolute;font-family:"Libre Baskerville",serif;font-size:17px;color:#333}
.stars{position:absolute;color:var(--gold);font-size:15px;letter-spacing:4px}
.arrow{position:absolute;top:4050px;width:44px;height:46px;background:var(--white);display:flex;align-items:center;justify-content:center}

/* strip + footer */
.notice{position:absolute;left:0;top:4239px;width:1200px;height:65px;background:var(--night);color:var(--white);font-size:14px;display:flex;align-items:center;justify-content:center}
.footer{position:absolute;left:0;top:4304px;width:1200px;height:357px;background:var(--night);color:var(--white)}
.footer h4{position:absolute;top:52px;font-family:"Libre Baskerville",serif;font-weight:400;font-size:17px;letter-spacing:.5px}
.footer ul{position:absolute;top:98px;list-style:none;font-size:15px;line-height:29px}
.footer li::before{content:"";display:inline-block;width:6px;height:6px;border-radius:50%;background:var(--gold);margin-right:14px;vertical-align:middle}
.contact-row{position:absolute;left:611px;display:flex;gap:20px;font-size:15px;line-height:26px;width:240px}
.contact-row svg{flex:none;margin-top:4px}
.footer .rule{position:absolute;left:80px;top:290px;width:1040px;height:1px;background:rgba(255,255,255,.12)}
.footer .copy{position:absolute;left:0;top:308px;width:1200px;text-align:center;font-size:13px}
</style>
</head>
<body>

<!-- Hero -->
<section class="hero" role="img" aria-label="Smiling couple embracing over a warm gold bokeh background">
  <nav class="nav">
    <a class="active" href="#" style="left:238px">Home</a>
    <a href="#" style="left:314px">Jewelry</a>
    <a href="#" style="left:399px">Services</a>
    <a href="#" style="left:745px">About</a>
    <a href="#" style="left:817px">Contact Us</a>
    <svg class="abs" style="left:918px;top:-2px" width="26" height="26" viewBox="0 0 26 26"><path d="M3 9h18l-2 12H5z" fill="none" stroke="#fff" stroke-width="1.8"/><path d="M8 9l4-5 4 5" fill="none" stroke="#fff" stroke-width="1.8"/><circle cx="22" cy="4" r="5" fill="var(--gold-soft)"/><text x="22" y="7" font-size="7" fill="#fff" text-anchor="middle" font-family="Poppins">0</text></svg>
    <svg class="abs" style="left:968px;top:0" width="24" height="24" viewBox="0 0 24 24"><circle cx="12" cy="12" r="12" fill="var(--gold-soft)"/><circle cx="12" cy="9" r="4" fill="#fff"/><path d="M5 19c2-4 12-4 14 0" fill="#fff"/></svg>
  </nav>
  <div class="brand" style="left:490px;top:20px;width:220px">
    <div class="name">BRILL'S</div>
    <div class="tag">YOUR HOMETOWN JEWELER</div>
  </div>
  <div class="hero-dots">
    <span style="top:277px"></span><span style="top:298px"></span>
    <span style="top:329px;width:14px;height:14px;left:29px;background:none;border:2px solid var(--gold-soft)"></span>
    <span style="top:361px"></span><span style="top:382px"></span>
  </div>
  <h1>YOUR HOMETOWN<br>JEWELERJUST GOT A<br>NEW HOME</h1>
  <div class="visit">VISIT US TODAY!</div>
  <a class="btn" href="#" style="left:105px;top:459px;width:167px;height:52px">SHOP NOW</a>
</section>

<!-- Intro -->
<section class="intro">
  <h2>BRILL'S<br>YOUR HOMETOWN<br>JEWELER</h2>
  <svg class="wave" style="left:78px;top:918px" viewBox="0 0 60 10"><path d="M0 7q5-6 10 0t10 0 10 0 10 0 10 0 10 0" fill="none" stroke="var(--gold)" stroke-width="2"/></svg>
  <div class="lead">Providing full jewelry services for you day in &amp; day out.</div>
  <p class="body" style="top:982px">Lorem Ipsum is simply dummy text of the printing and typesetting industry. Lorem Ipsum has been the indu stry's standard dummy text ever since the</p>
  <p class="body" style="top:1077px">Lorem Ipsum is simply dummy text of the printing and typesetting industry. Lorem Ipsum has been the industry's standard dummy text ever since the 1500s, when an unknown printer took a galley/</p>
  <div class="photo" role="img" aria-label="Hand holding a diamond engagement ring" style="left:706px;top:742px;width:417px;height:483px;background:linear-gradient(135deg,#f4eedc 40%,#e8c9a8 75%,#d9b08e)"></div>
</section>

<!-- Jewelry grid -->
<section>
  <h2 class="section-title" style="top:1296px">JEWELRY &amp; DIMONDS</h2>
  <div class="subtitle" style="top:1350px">providing full jewelry services for you day in and day out.</div>
  <svg class="wave" style="left:570px;top:1382px" viewBox="0 0 60 10"><path d="M0 7q5-6 10 0t10 0 10 0 10 0 10 0 10 0" fill="none" stroke="var(--gold)" stroke-width="2"/></svg>
  <div class="photo" role="img" aria-label="Silver diamond necklace on a dark display bust" style="left:136px;top:1433px;width:454px;height:277px;background:linear-gradient(180deg,#4a1f28,#6a5a5e 60%,#8c8a8e)"></div>
  <div class="photo" role="img" aria-label="Delicate silver chain necklace on cream fabric" style="left:609px;top:1433px;width:219px;height:145px;background:linear-gradient(135deg,#efe9dc,#d6d0c2)"></div>
  <div class="photo" role="img" aria-label="Diamond ring on a dark wood surface" style="left:843px;top:1433px;width:219px;height:145px;background:linear-gradient(135deg,#4a3a36,#2b2422)"></div>
  <div class="photo" role="img" aria-label="Gold wristwatch on a pale stand" style="left:609px;top:1593px;width:453px;height:277px;background:linear-gradient(180deg,#dfe8ea,#c9d3d4 70%,#e6dcb0)"></div>
  <div class="photo" role="img" aria-label="Pearl bracelet on white" style="left:136px;top:1725px;width:219px;height:145px;background:linear-gradient(180deg,#f2f2f2,#dcdcdc)"></div>
  <div class="photo" role="img" aria-label="Colored gemstone jewelry category" style="left:371px;top:1725px;width:219px;height:145px;background:var(--gold-deep)"></div>
  <div class="abs serif" style="left:371px;top:1780px;width:219px;text-align:center;color:#fff;font-size:23px">Colored</div>
  <div class="explore">Explore More <svg width="10" height="12" viewBox="0 0 10 12"><path d="M2 1l6 5-6 5z" fill="var(--gold)"/></svg></div>
</section>

<!-- Lifetime guarantee -->
<section>
  <div class="lifetime"></div>
  <div class="photo" role="img" aria-label="Diamond bangles and a halo ring on a cream cushion" style="left:0;top:1964px;width:290px;height:366px;background:linear-gradient(135deg,#e9dfc6,#d8c9a3);border-radius:0 30px 30px 0"></div>
  <h2 class="section-title" style="top:2060px;line-height:47px">LIFETIME SATIFACTION<br>GUARANTEED</h2>
  <div class="perk" style="top:2186px">45 Days Return</div>
  <div class="perk" style="top:2228px">Lifetime Warranty</div>
  <div class="perk" style="top:2270px">Lifetime Upgrade</div>
  <a class="btn" href="#" style="left:502px;top:2320px;width:196px;height:55px">GET STARTED</a>
</section>

<!-- About -->
<section>
  <div class="photo" role="img" aria-label="Black and white photo of two hands wearing wedding rings" style="left:510px;top:2521px;width:573px;height:415px;background:linear-gradient(135deg,#2a2a2a,#8a8a8a 55%,#3a3a3a)"></div>
  <div class="about-card">
    <h2>ABOUT US</h2>
    <svg class="wave" style="left:230px;top:100px" viewBox="0 0 60 10"><path d="M0 7q5-6 10 0t10 0 10 0 10 0 10 0 10 0" fill="none" stroke="var(--gold)" stroke-width="2"/></svg>
    <p>Lorem Ipsum is simply dummy text of the printing and typesetting industry. Lorem Ipsum has been the indu stry's standard dummy text ever since the Lorem Ipsum is simply dummy text of the printing and typesetting industry.</p>
  </div>
</section>

<!-- Instagram -->
<section>
  <h2 class="section-title" style="top:3015px">OUR INSTAGRAM</h2>
  <svg class="wave" style="left:570px;top:3070px" viewBox="0 0 60 10"><path d="M0 7q5-6 10 0t10 0 10 0 10 0 10 0 10 0" fill="none" stroke="var(--gold)" stroke-width="2"/></svg>
  <div class="photo" role="img" aria-label="Gift box with pink ribbon" style="left:77px;top:3115px;width:159px;height:145px;background:linear-gradient(135deg,#d8d2c8,#f0e2e4)"></div>
  <div class="photo" role="img" aria-label="Diamond cluster ring on teal" style="left:254px;top:3115px;width:159px;height:145px;background:linear-gradient(135deg,#2f5260,#9aa4a6)"></div>
  <div class="photo" role="img" aria-label="Solitaire ring in a red box" style="left:431px;top:3115px;width:159px;height:145px;background:linear-gradient(180deg,#f0eeea,#c23a2f)"></div>
  <div class="photo" role="img" aria-label="Model wearing a statement necklace" style="left:609px;top:3115px;width:159px;height:145px;background:linear-gradient(135deg,#3a2b26,#a98a7a)"></div>
  <div class="photo" role="img" aria-label="Couple embracing" style="left:786px;top:3115px;width:159px;height:145px;background:linear-gradient(135deg,#6fa0b5,#d6b9a0)"></div>
  <div class="photo" role="img" aria-label="Diamond ring close-up" style="left:963px;top:3115px;width:159px;height:145px;background:linear-gradient(135deg,#c9c7c2,#6c6a66)"></div>
  <a class="btn" href="#" style="left:509px;top:3290px;width:182px;height:57px">FOLLOW US</a>
</section>

<!-- Services -->
<section>
  <h2 class="section-title" style="top:3462px">OUR SERVICES</h2>
  <svg class="wave" style="left:570px;top:3518px" viewBox="0 0 60 10"><path d="M0 7q5-6 10 0t10 0 10 0 10 0 10 0 10 0" fill="none" stroke="var(--gold)" stroke-width="2"/></svg>
  <div class="service" style="left:172px">
    <svg width="66" height="66" viewBox="0 0 66 66" fill="none" stroke="#222" stroke-width="2"><path d="M42 8a14 14 0 0 0-12 19L8 49l9 9 22-22a14 14 0 0 0 19-12l-8 5-8-3-3-8z"/><circle cx="14" cy="52" r="2" fill="var(--gold)" stroke="none"/></svg>
    <h3>Repairs</h3><p>Lorem Ipsum is simply text of the print</p>
  </div>
  <div class="service" style="left:392px">
    <svg width="66" height="66" viewBox="0 0 66 66" fill="none" stroke="#222" stroke-width="2"><path d="M33 14l5 12 13 1-10 8 3 13-11-7-11 7 3-13-10-8 13-1z" fill="var(--gold-soft)"/><path d="M33 2v6M8 24l5 2M58 24l-5 2M14 58l4-4M52 58l-4-4"/></svg>
    <h3>Appraisals</h3><p>Lorem Ipsum is simply text of the print</p>
  </div>
  <div class="service" style="left:610px">
    <svg width="66" height="66" viewBox="0 0 66 66" fill="none" stroke="#222" stroke-width="2"><path d="M10 52h22l-4-14H14z" fill="var(--gold-soft)"/><path d="M34 52h22l-4-14H38z"/><path d="M22 36h22l-4-14H26z"/></svg>
    <h3>Buying Gold</h3><p>Lorem Ipsum is simply text of the print</p>
  </div>
  <div class="service" style="left:829px">
    <svg width="66" height="66" viewBox="0 0 66 66" fill="none" stroke="#222" stroke-width="2"><path d="M33 6l5 6 8-2 2 8 7 4-3 7 3 7-7 4-2 8-8-2-5 6-5-6-8 2-2-8-7-4 3-7-3-7 7-4 2-8 8 2z"/><path d="M24 34l7 7 13-14" stroke="var(--gold)" stroke-width="3"/></svg>
    <h3>Custom</h3><p>Lorem Ipsum is simply text of the print</p>
  </div>
</section>

<!-- Happy clients -->
<section>
  <div class="clients"></div>
  <h2 class="section-title" style="top:3908px">HAPPY CLIENTS</h2>
  <svg class="wave" style="left:570px;top:3963px" viewBox="0 0 60 10"><path d="M0 7q5-6 10 0t10 0 10 0 10 0 10 0 10 0" fill="none" stroke="var(--gold)" stroke-width="2"/></svg>
  <div class="arrow" style="left:0"><svg width="12" height="20" viewBox="0 0 12 20"><path d="M10 2L2 10l8 8" fill="none" stroke="#999" stroke-width="1.5"/></svg></div>
  <div class="arrow" style="left:1156px"><svg width="12" height="20" viewBox="0 0 12 20"><path d="M2 2l8 8-8 8" fill="none" stroke="#999" stroke-width="1.5"/></svg></div>

  <div class="photo" role="img" aria-label="Client portrait" style="left:77px;top:4025px;width:115px;height:115px;border-radius:50%;background:linear-gradient(135deg,#b89a6a,#7a5a3a)"></div>
  <p class="review" style="left:217px">Lorem Ipsum is simply dummy text of the is printing and typesetting industry Lorem the Ipsum has been the indu...</p>
  <div class="client-name" style="left:219px;top:4138px">— Client Name</div>
  <div class="stars" style="left:244px;top:4162px">★★★★★</div>

  <div class="photo" role="img" aria-label="Client portrait" style="left:633px;top:4025px;width:115px;height:115px;border-radius:50%;background:linear-gradient(135deg,#b89a6a,#7a5a3a)"></div>
  <p class="review" style="left:773px">Lorem Ipsum is simply dummy text of the is printing and typesetting industry Lorem the Ipsum has been the indu...</p>
  <div class="client-name" style="left:775px;top:4138px">— Client Name</div>
  <div class="stars" style="left:800px;top:4162px">★★★★<span style="color:#ccc">★</span></div>
</section>

<div class="notice">Did you know All our Dimonds Come with a Life Time Waranty &amp; 100 % Satisfaction guarantee</div>

<!-- Footer -->
<footer class="footer">
  <h4 style="left:80px">SITEMAP</h4>
  <ul style="left:80px"><li>Home</li><li>Jewelry</li><li>Services</li><li>About</li><li>Contcat</li></ul>
  <h4 style="left:346px">QUICKLINKS</h4>
  <ul style="left:346px"><li>Login/register</li><li>Order History</li><li>Shopping Cat</li><li>Whish List</li><li>Newsletter</li></ul>
  <h4 style="left:611px">CONTACT INFO</h4>
  <div class="contact-row" style="top:98px">
    <svg width="20" height="24" viewBox="0 0 20 24"><path d="M10 1a8 8 0 0 0-8 8c0 6 8 14 8 14s8-8 8-14a8 8 0 0 0-8-8z" fill="none" stroke="var(--gold)" stroke-width="2"/><circle cx="10" cy="9" r="3" fill="var(--gold)"/></svg>
    <span>418 Palm Vista Way, Harbor Glen, NV 89900</span>
  </div>
  <div class="contact-row" style="top:164px">
    <svg width="20" height="16" viewBox="0 0 20 16"><rect x="1" y="1" width="18" height="14" rx="1" fill="var(--gold)"/><path d="M1 2l9 7 9-7" fill="none" stroke="var(--night)" stroke-width="1.5"/></svg>
    <span style="word-break:break-all">hello@brillsjewelers-example.com</span>
  </div>
  <div class="contact-row" style="top:222px">
    <svg width="20" height="20" viewBox="0 0 20 20"><path d="M4 1l4 4-2 3c1 2 4 5 6 6l3-2 4 4-3 3C9 19 1 11 1 4z" fill="var(--gold)"/></svg>
    <span>(555)014-2286</span>
  </div>
  <div class="brand" style="left:895px;top:118px;width:205px">
    <div class="name">BRILL'S</div>
    <div class="tag">YOUR HOMETOWN JEWELER</div>
  </div>
  <div class="abs" style="left:968px;top:240px;width:46px;height:46px;border-radius:50%;background:var(--gold)"></div>
  <div class="rule"></div>
  <div class="copy">©BRILL'S - 2020 All rights reserved.</div>
</footer>

</body>
</html>
```